Poly Gel bottle Design that stands out for Nail Company

I need a label design for the poly gel polish bottle. We are looking for a design that fit our brand store color and a clean design similar to our competitor.

We have 3 bottle Title: Gel Top Coat, Gel base Coat, Gel Matte Coat
The bottle will be white.

Also I will need 1 label for the extension gel.

Bottle volume is 15ml/0.5 fl oz

Target Market(s)

beauty acrylic nail and poly gel nail

Industry/Entity Type

Nail

Font styles to use
Serif
Decorative

Colors
6c459b

Requirements
Must have
• store color scheme. www.tealpebbleshop.com

```html
<!DOCTYPE html>
<html lang="en">
<head>
<meta charset="utf-8">
<title>teal pebble – Gel Coat Labels</title>
<link href="https://fonts.googleapis.com/css2?family=Josefin+Sans:wght@600;700&family=Poppins:wght@400;600;700&display=swap" rel="stylesheet">
<style>
  :root {
    --bg-top: #bebebe;
    --bg-bottom: #f5f6fc;
    --watermark: #d9d9d9;
    --label: #ffffff;
    --label-edge: #e3e4ec;
    --ink: #000000;
    --rose-a: #c9928f;
    --rose-b: #f0c9c9;
    --rose-c: #a8716d;
    --gold-a: #b98f3a;
    --gold-b: #e6e0a4;
    --gold-c: #8f6a24;
    --silver-a: #a9aaad;
    --silver-b: #f1f1f3;
    --silver-c: #9b9ca0;
  }
  * { margin: 0; padding: 0; box-sizing: border-box; }
  html, body { width: 1190px; height: 1200px; overflow: hidden; }
  body {
    font-family: "Poppins", sans-serif;
    background: linear-gradient(180deg, var(--bg-top) 0%, var(--bg-bottom) 80%);
    position: relative;
  }
  .brand-backdrop {
    position: absolute;
    top: 60px; left: 0; width: 100%;
    text-align: center;
    font-family: "Josefin Sans", sans-serif;
    font-weight: 600;
    font-size: 170px;
    line-height: 1.2;
    color: var(--watermark);
  }
  .label-row {
    position: absolute;
    top: 400px; left: 0; width: 100%;
    display: flex; justify-content: center; gap: 22px;
  }
  .label {
    width: 360px; height: 700px;
    background: var(--label);
    border: 1px solid var(--label-edge);
    border-radius: 40px 40px 56px 56px;
    display: flex; flex-direction: column; align-items: center; justify-content: center;
    box-shadow: 0 18px 28px rgba(0,0,0,0.10);
  }
  .label--center { transform: translateY(14px); }
  .label__brand {
    font-family: "Josefin Sans", sans-serif;
    font-weight: 700;
    font-size: 56px;
    color: var(--ink);
    line-height: 1;
    white-space: nowrap;
  }
  .label__type {
    margin-top: 40px;
    font-weight: 600;
    font-size: 32px;
    letter-spacing: 5px;
    color: var(--ink);
    line-height: 1;
    white-space: nowrap;
  }
  .label__coat {
    margin-top: 4px;
    width: 224px;
    text-align: center;
    font-weight: 700;
    font-size: 64px;
    line-height: 68px;
    color: var(--ink);
    border-radius: 4px;
  }
  .label__coat--rose { background: linear-gradient(90deg, var(--rose-a), var(--rose-b) 45%, var(--rose-c)); }
  .label__coat--gold { background: linear-gradient(90deg, var(--gold-a), var(--gold-b) 55%, var(--gold-c)); }
  .label__coat--silver { background: linear-gradient(90deg, var(--silver-a), var(--silver-b) 45%, var(--silver-c)); }
  .label__cure {
    margin-top: 10px;
    font-size: 15px;
    color: var(--ink);
    white-space: nowrap;
  }
  .label__volume {
    margin-top: 22px;
    font-size: 15px;
    color: var(--ink);
    white-space: nowrap;
  }
</style>
</head>
<body>
  <div class="brand-backdrop">teal pebble</div>

  <main class="label-row">
    <section class="label">
      <div class="label__brand">teal pebble</div>
      <div class="label__type">GEL MATTE</div>
      <div class="label__coat label__coat--rose">COAT</div>
      <div class="label__cure">SOAK-OFF UV / LED CURED</div>
      <div class="label__volume">15ML ℮ 0.5 FL OZ</div>
    </section>

    <section class="label label--center">
      <div class="label__brand">teal pebble</div>
      <div class="label__type">GEL TOP</div>
      <div class="label__coat label__coat--gold">COAT</div>
      <div class="label__cure">SOAK-OFF UV / LED CURED</div>
      <div class="label__volume">15ML ℮ 0.5 FL OZ</div>
    </section>

    <section class="label">
      <div class="label__brand">teal pebble</div>
      <div class="label__type">GEL BASE</div>
      <div class="label__coat label__coat--silver">COAT</div>
      <div class="label__cure">SOAK-OFF UV / LED CURED</div>
      <div class="label__volume">15ML ℮ 0.5 FL OZ</div>
    </section>
  </main>
</body>
</html>
```